Harbourgate Earthmoving – Website Design Brief

Web Design Brief

We are seeking a web designer to build a modern, responsive website for Harbourgate Earthmoving, a Sydney-based earthworks and excavation company.

2. Project Goal
- Build a professional, easy-to-navigate website that:
- Showcases HGE’s capabilities and past projects
- Attracts residential and commercial developers
- Builds credibility and encourages enquiries

3. Target Audience
- Residential developers and home builders
- Commercial construction firms
- Project managers seeking reliable excavation & plant hire services

4. Services to Highlight
- Bulk Excavation
- Detailed Excavation
- Demolition
- Shoring
- Plant Hire

5. Brand Style & Tone
- Clean, bold, and modern
- Professional with a “we get the job done” attitude
- Colors: Lime Green + Concrete Grey (from logo)
- Fonts: Match the modern, rounded, bold typeface in the logo
- Imagery: Showcase big machines, on-site work, before & after shots

6. Website Pages
Recommended structure:
- Home – Quick intro, project highlights, CTA
- About Us – Team story, mission, safety focus
- Services – Separate sections for each core service
- Projects – Case studies or photo gallery
- Plant Hire – Machines available, specs/photos
- Contact – Form + map + details

7. Assets Provided
- Logo (both long + stacked formats)
- Project photos. More can be provided if required.
- Copy: To be drafted

8. Deliverables
Responsive website (desktop/mobile/tablet)
- SEO-ready structure
- CMS (WordPress) for future edits
- Google Maps integration, job enquiry form

Target Market(s)

Target Audience Residential developers and home builders Commercial construction firms Project managers seeking reliable excavation & plant hire services

Industry/Entity Type

Construction

Number of Pages Required

1 page

Requirements
Must have
• Build a professional, easy-to-navigate website that: Showcases HGE’s capabilities and past projects Attracts residential and commercial developers Builds credibility and encourages enquiries
Nice to have
• All provided in the Description
Should not have

```html
<!DOCTYPE html>
<html lang="en">
<head>
<meta charset="utf-8">
<title>Harbourgate Earthmoving – Earthworks &amp; Excavation Sydney</title>
<link rel="stylesheet" href="https://fonts.googleapis.com/css2?family=Montserrat:wght@500;600;700;800&family=Lato:wght@400;700&display=swap">
<style>
:root{
  --green:#86c440;
  --green-dark:#74ad33;
  --grey:#575757;
  --grey-dark:#4a4a4a;
  --ink:#333333;
  --text:#555555;
  --muted:#8a8a8a;
  --line:#e6e6e6;
  --white:#ffffff;
}
*{box-sizing:border-box;margin:0;padding:0}
html,body{width:1200px;height:4073px;overflow:hidden}
body{position:relative;background:var(--white);font-family:'Lato',sans-serif;color:var(--text)}
.abs{position:absolute}
h1,h2,h3,h4,.display{font-family:'Montserrat',sans-serif;color:var(--ink)}
a{color:inherit;text-decoration:none}

/* top bar */
.topbar{left:0;top:0;width:1200px;height:33px;border-bottom:1px solid var(--line)}
.topbar__links{left:163px;top:11px;display:flex;gap:26px;font-size:8px;letter-spacing:.5px;color:var(--muted)}
.topbar__social{left:966px;top:11px;display:flex;gap:11px}
.topbar__social span{width:8px;height:8px;border-radius:50%;background:var(--green)}

/* nav */
.brand{left:163px;top:48px;font-family:'Montserrat',sans-serif;font-weight:800;font-size:20px;color:var(--green);letter-spacing:.3px}
.nav{left:626px;top:53px;display:flex;gap:19px;font-size:13px;color:var(--muted)}
.nav .is-active{color:var(--green)}

/* hero */
.hero{left:0;top:90px;width:1200px;height:563px;background:linear-gradient(180deg,#7f8792 0%,#6d737b 55%,#4d5358 100%)}
.hero__title{left:163px;top:245px;width:560px;font-size:35px;line-height:44px;font-weight:700;color:var(--white);text-decoration:underline;text-decoration-thickness:2px;text-underline-offset:5px}
.hero__lead{left:163px;top:375px;width:520px;font-size:14px;line-height:23px;color:var(--white)}
.btn{display:flex;align-items:center;justify-content:center;background:var(--green);color:var(--white);font-size:11px;font-weight:700}
.hero__btn{left:163px;top:458px;width:166px;height:39px;text-decoration:underline}

.stat{top:653px;width:187px;height:146px;padding:38px 0 0 26px;color:var(--white)}
.stat--green{background:var(--green)}
.stat--grey{background:var(--grey)}
.stat__num{font-family:'Montserrat',sans-serif;font-weight:700;font-size:52px;line-height:56px}
.stat__num small{font-size:36px;font-weight:500}
.stat__rule{width:74px;height:3px;background:var(--white);margin:4px 0 6px}
.stat__label{font-size:12px;text-decoration:underline}

.intro-card{left:724px;top:519px;width:313px;height:341px;background:var(--white);border-top:5px solid var(--green);box-shadow:0 4px 22px rgba(0,0,0,.12);padding:22px 26px}
.intro-card h3{font-size:19px;line-height:24px;font-weight:600;margin-bottom:20px}
.intro-item{display:flex;gap:14px;margin-bottom:18px}
.intro-item svg{flex:0 0 42px}
.intro-item h4{font-family:'Lato',sans-serif;font-size:10px;font-weight:700;color:var(--ink);text-decoration:underline;margin-bottom:4px}
.intro-item p{font-size:9.5px;line-height:16px;color:var(--green-dark);text-decoration:underline}

/* about */
.eyebrow{font-size:7.5px;letter-spacing:.6px;color:var(--green);font-weight:700}
.about__eyebrow{left:163px;top:1015px}
.about__title{left:163px;top:1030px;width:480px;font-size:31px;line-height:41px;font-weight:600}
.about__text{left:163px;top:1128px;width:455px;font-size:9.8px;line-height:17.5px}
.about__btn{left:163px;top:1243px;width:177px;height:39px}
.frame{background:var(--white);box-shadow:0 3px 16px rgba(0,0,0,.14);padding:11px}
.frame div{width:100%;height:100%}
.about__photo-back{left:756px;top:958px;width:281px;height:244px}
.about__photo-front{left:666px;top:1091px;width:223px;height:245px}
.about__play{left:726px;top:1069px;width:60px;height:50px;background:var(--green);display:flex;align-items:center;justify-content:center}

/* services */
.service{top:1398px;width:240px;height:375px;padding:40px 33px;color:var(--white)}
.service--photo{background:linear-gradient(180deg,#6c6c6c 0%,#5a5a5a 60%,#474747 100%)}
.service--green{background:linear-gradient(180deg,#8fcc4a 0%,#86c440 60%,#7bb63a 100%)}
.service h3{color:var(--white);font-size:22px;line-height:30px;font-weight:600;margin-bottom:20px}
.service p{font-size:10px;line-height:17.5px;color:rgba(255,255,255,.85)}
.service__arrow{left:175px;top:316px;width:37px;height:33px;display:flex;align-items:center;justify-content:center}
.service--photo .service__arrow{background:var(--green)}
.service--green .service__arrow{background:var(--grey-dark)}

/* projects */
.section-head{left:0;width:1200px;text-align:center}
.section-head .eyebrow{display:block;margin-bottom:10px}
.section-head h2{font-size:32px;font-weight:600}
.tile{display:block}
.tile--feature{background:var(--green);display:flex;flex-direction:column;align-items:center;justify-content:center;color:var(--white)}
.tile--feature small{font-size:7.5px;letter-spacing:.5px;margin-bottom:7px}
.tile--feature strong{font-size:11px;font-weight:400;margin-bottom:20px}
.tile--feature span{width:30px;height:22px;background:var(--white);color:var(--green);display:flex;align-items:center;justify-content:center;font-size:12px}

/* map + contact */
.map{left:0;top:2392px;width:1200px;height:379px;background:radial-gradient(ellipse at 60% 40%,#b9c6d2 0%,#9fb1c0 50%,#7f8f9c 100%)}
.address-card{left:231px;top:2693px;width:300px;height:178px;background:var(--white);border-top:5px solid var(--green);box-shadow:0 4px 20px rgba(0,0,0,.1);padding:42px 31px}
.address-card small{font-size:7.5px;letter-spacing:.5px;color:var(--text)}
.address-card p{font-family:'Montserrat',sans-serif;font-weight:600;font-size:17.5px;line-height:23px;color:var(--ink);margin-top:9px}
.contact{top:2782px;display:flex;gap:18px}
.contact__icon{width:40px;height:40px;background:var(--green);display:flex;align-items:center;justify-content:center;margin-top:10px}
.contact small{display:block;font-size:7.5px;letter-spacing:.4px;color:var(--text);margin-bottom:6px}
.contact p{font-size:12.5px;line-height:19px;color:var(--ink)}

/* testimonials */
.testi__photo{left:163px;top:3013px;width:289px;height:277px}
.quote-mark{left:498px;top:3054px;width:66px;height:50px;background:var(--green);display:flex;align-items:center;justify-content:center;font-family:'Montserrat',sans-serif;font-weight:800;font-size:40px;color:var(--white);line-height:1;padding-top:14px}
.testi__text{left:498px;top:3122px;width:530px;font-size:10.5px;line-height:17.5px}
.testi__name{left:498px;top:3190px;font-family:'Montserrat',sans-serif;font-weight:600;font-size:13px;color:var(--ink)}
.testi__role{left:498px;top:3209px;font-size:8px;color:var(--green)}
.dots{display:flex;gap:10px}
.dots span{width:7px;height:7px;border-radius:50%;background:var(--grey-dark)}
.dots span:first-child{background:var(--green)}

/* video band */
.video{left:0;top:3353px;width:1200px;height:415px;background:linear-gradient(160deg,#4f7f98 0%,#6f8a7a 35%,#a07a66 65%,#8a8f95 100%)}
.video__play{left:561px;top:3486px;width:78px;height:79px;background:rgba(255,255,255,.6);display:flex;align-items:center;justify-content:center}

/* footer */
.footer-brand{left:0;top:3768px;width:468px;height:305px;background:var(--green);padding:38px 0 0 168px;color:var(--white)}
.footer-brand__logo{font-family:'Montserrat',sans-serif;font-weight:800;font-size:20px;line-height:22px;color:var(--white);width:120px}
.footer-brand small{display:block;font-size:7.5px;margin-top:14px}
.footer-brand__phone{font-family:'Montserrat',sans-serif;font-weight:700;font-size:19px;margin-top:6px}
.footer-brand__social{display:flex;gap:12px;margin-top:16px}
.footer-brand__social span{width:23px;height:23px;border-radius:50%;background:var(--white)}
.footer-brand p{font-size:9.5px;line-height:16px;margin-top:18px;width:210px}
.footer-main{left:468px;top:3768px;width:732px;height:305px;background:var(--grey)}
.fcol{top:3818px;color:var(--white)}
.fcol h4{font-family:'Montserrat',sans-serif;font-weight:500;font-size:12px;color:var(--white);margin-bottom:16px}
.fcol ul{list-style:none;font-size:9.5px;line-height:21px;color:rgba(255,255,255,.85)}
.news h5{font-family:'Lato',sans-serif;font-weight:400;font-size:10px;line-height:15px;color:var(--white)}
.news small{display:block;font-size:7px;color:rgba(255,255,255,.6);margin:3px 0 12px}
.footer-dots{display:flex;gap:5px}
.footer-dots span{width:4px;height:4px;border-radius:50%;background:rgba(255,255,255,.7)}
.copyright{left:530px;top:4007px;font-size:9.5px;color:rgba(255,255,255,.85)}
</style>
</head>
<body>

<header>
  <div class="abs topbar"></div>
  <nav class="abs topbar__links"><a>SUPPORT</a><a>PARTNERS</a><a>CAREERS</a></nav>
  <div class="abs topbar__social" aria-label="Social links"><span></span><span></span><span></span><span></span></div>
  <a class="abs brand">Harbourgate Earthmoving</a>
  <nav class="abs nav"><a class="is-active">Home</a><a>Services ▾</a><a>Projects</a><a>Plant Hire</a><a>About Us</a><a>Contacts</a></nav>
</header>

<section>
  <div class="abs hero" role="img" aria-label="Company utility truck and tipper trucks parked at a misty excavation site"></div>
  <h1 class="abs hero__title">Expert Earthworks &amp; Excavation Services in Sydney</h1>
  <p class="abs hero__lead">Reliable, professional, and on-time solutions for residential, commercial, and civil construction projects.</p>
  <a class="abs btn hero__btn">Learn more →</a>

  <div class="abs stat stat--green" style="left:163px"><div class="stat__num">30</div><div class="stat__rule"></div><div class="stat__label">Running Projects</div></div>
  <div class="abs stat stat--grey" style="left:350px"><div class="stat__num">147</div><div class="stat__rule"></div><div class="stat__label">Completed Projects</div></div>
  <div class="abs stat stat--green" style="left:537px"><div class="stat__num">25<small>+</small></div><div class="stat__rule"></div><div class="stat__label">Years of Expirience</div></div>

  <div class="abs intro-card">
    <h3>We Build and Manage Spaces That Shape the Future</h3>
    <div class="intro-item">
      <svg width="42" height="42" viewBox="0 0 42 42" fill="none" stroke="#86c440" stroke-width="2"><path d="M8 24a13 13 0 0 1 26 0"/><path d="M5 24h32v4H5z"/><path d="M21 11v8"/><path d="M12 30c2 6 16 6 18 0"/></svg>
      <div><h4>Residential developers &amp; home builders</h4><p>Expert site prep and excavation for smooth residential builds.</p></div>
    </div>
    <div class="intro-item">
      <svg width="42" height="42" viewBox="0 0 42 42" fill="none" stroke="#86c440" stroke-width="2"><path d="M6 4h8v34H6z"/><path d="M14 30h22v8H14z"/><path d="M14 10l18 18"/></svg>
      <div><h4>Commercial Construction Firms</h4><p>Dependable earthworks tailored to complex commercial projects.</p></div>
    </div>
    <div class="intro-item">
      <svg width="42" height="42" viewBox="0 0 42 42" fill="none" stroke="#86c440" stroke-width="2"><path d="M4 8h34v6H4z"/><path d="M18 14v24"/><path d="M26 14v10"/><path d="M10 14v8"/></svg>
      <div><h4>Excavation &amp; Plant Hire Services</h4><p>Modern equipment and skilled operators ready for any job.</p></div>
    </div>
  </div>
</section>

<section>
  <span class="abs eyebrow about__eyebrow">ABOUT US</span>
  <h2 class="abs about__title">With our knowledge we guarente success</h2>
  <p class="abs about__text">Harbourgate Earthmoving is a specialised earthworks &amp; excavation company offering a comprehensive range of services including bulk &amp; detailed excavation, demolition, shoring and plant hire. Equipped with Advanced equipment and a skilled team, the company delivers efficient, safe and tailored solutions for residential, commercial and infrastructure projects.</p>
  <a class="abs btn about__btn">Learn more →</a>
  <div class="abs frame about__photo-back"><div role="img" aria-label="Site plans, notebook and tools on a timber desk" style="background:linear-gradient(135deg,#c79a63,#a8784a 60%,#6b5a48)"></div></div>
  <div class="abs frame about__photo-front"><div role="img" aria-label="Excavator clearing demolition rubble beside a company truck" style="background:linear-gradient(180deg,#a9b2ba,#8d8a80 55%,#7a7570)"></div></div>
  <div class="abs about__play"><svg width="18" height="20" viewBox="0 0 18 20"><path d="M2 1l15 9-15 9z" fill="#fff"/></svg></div>
</section>

<section>
  <article class="abs service service--photo" style="left:0" role="img" aria-label="Excavator bucket at a bulk earthworks site">
    <h3>Bulk<br>Excavation</h3><p>Large-scale earth removal for site preparation, leveling, and groundwork on construction projects.</p>
    <a class="abs service__arrow"><svg width="14" height="10" viewBox="0 0 14 10"><path d="M0 5h12M8 1l4 4-4 4" stroke="#fff" stroke-width="2" fill="none"/></svg></a>
  </article>
  <article class="abs service service--green" style="left:240px" role="img" aria-label="Machine digging footings on site">
    <h3>Detailed<br>Excavation</h3><p>Precise digging around foundations, footings, and structures with a focus on accuracy and safety.</p>
    <a class="abs service__arrow"><svg width="14" height="10" viewBox="0 0 14 10"><path d="M0 5h12M8 1l4 4-4 4" stroke="#fff" stroke-width="2" fill="none"/></svg></a>
  </article>
  <article class="abs service service--photo" style="left:480px" role="img" aria-label="Building being demolished with dust">
    <h3>Demolition</h3><p>Safe and efficient demolition of structures, clearing the way for new development.</p>
    <a class="abs service__arrow"><svg width="14" height="10" viewBox="0 0 14 10"><path d="M0 5h12M8 1l4 4-4 4" stroke="#fff" stroke-width="2" fill="none"/></svg></a>
  </article>
  <article class="abs service service--green" style="left:720px" role="img" aria-label="Piling rig installing shoring on site">
    <h3>Shoring</h3><p>Structural support solutions to stabilize excavation sites and prevent ground collapse.</p>
    <a class="abs service__arrow"><svg width="14" height="10" viewBox="0 0 14 10"><path d="M0 5h12M8 1l4 4-4 4" stroke="#fff" stroke-width="2" fill="none"/></svg></a>
  </article>
  <article class="abs service service--photo" style="left:960px" role="img" aria-label="Row of excavators available for hire">
    <h3>Plant Hire</h3><p>Modern, well-maintained machinery available for short or long-term hire with skilled operators.</p>
    <a class="abs service__arrow"><svg width="14" height="10" viewBox="0 0 14 10"><path d="M0 5h12M8 1l4 4-4 4" stroke="#fff" stroke-width="2" fill="none"/></svg></a>
  </article>
</section>

<section>
  <div class="abs section-head" style="top:1835px"><span class="eyebrow">OUR WORKS</span><h2>Our Special Projects</h2></div>
  <div class="abs tile" style="left:163px;top:1916px;width:281px;height:411px;background:linear-gradient(180deg,#b4bcc3,#8f8a7e 55%,#9a9890)" role="img" aria-label="Excavators working on a demolition site next to a truck"></div>
  <div class="abs tile" style="left:460px;top:1916px;width:281px;height:199px;background:linear-gradient(180deg,#c9d2da,#8a7a66 55%,#6f5f4e)" role="img" aria-label="Levelled earth pad with excavator"></div>
  <div class="abs tile" style="left:756px;top:1916px;width:281px;height:199px;background:linear-gradient(180deg,#7fa9d6,#8c9a72 45%,#8c6e52)" role="img" aria-label="Basement excavation in a residential street"></div>
  <a class="abs tile tile--feature" style="left:460px;top:2128px;width:281px;height:199px"><small>COMMERCIAL</small><strong>Sydney Earthworks</strong><span>+</span></a>
  <div class="abs tile" style="left:756px;top:2128px;width:281px;height:199px;background:linear-gradient(180deg,#b7c3cf,#8a8478 50%,#5f5a55)" role="img" aria-label="City construction site with tower crane"></div>
</section>

<section>
  <div class="abs map" role="img" aria-label="Hand pointing at a location on a paper map"></div>
  <svg class="abs" style="left:587px;top:2567px" width="26" height="36" viewBox="0 0 26 36"><path d="M13 0C6 0 1 5 1 12c0 9 12 24 12 24s12-15 12-24C25 5 20 0 13 0z" fill="#86c440"/><circle cx="13" cy="12" r="5" fill="#fff"/></svg>
  <div class="abs address-card"><small>COMPANY ADDRESS</small><p>Harbourgate Earthmoving Pty Ltd, Unit 4, 22 Carrow Rd, Ashbury NSW</p></div>
  <div class="abs contact" style="left:569px">
    <div class="contact__icon"><svg width="20" height="20" viewBox="0 0 24 24"><path d="M6 2l4 4-2 3c1 3 4 6 7 7l3-2 4 4-3 4C10 22 2 14 2 5z" fill="none" stroke="#fff" stroke-width="1.8"/></svg></div>
    <div><small>COMPANY PHONES</small><p>+61 400 555 124<br>+61 400 555 125</p></div>
  </div>
  <div class="abs contact" style="left:764px">
    <div class="contact__icon"><svg width="22" height="22" viewBox="0 0 24 24"><circle cx="12" cy="12" r="9" fill="none" stroke="#fff" stroke-width="1.8"/><circle cx="8" cy="12" r="1.3" fill="#fff"/><circle cx="12" cy="12" r="1.3" fill="#fff"/><circle cx="16" cy="12" r="1.3" fill="#fff"/></svg></div>
    <div><small>DIRECT EMAILS</small><p>info@hge.com<br>support@hge.com</p></div>
  </div>
</section>

<section>
  <div class="abs section-head" style="top:2933px"><span class="eyebrow">TESTIMONIALS</span><h2>Our Clients Say</h2></div>
  <div class="abs frame testi__photo"><div role="img" aria-label="Two people shaking hands over a desk" style="background:linear-gradient(135deg,#eeeae4,#d8c8b4 50%,#b8a48e)"></div></div>
  <div class="abs quote-mark">”</div>
  <p class="abs testi__text">Working with Harbourgate Earthmoving was seamless from start to finish. The team was professional, communicated clearly, and completed the excavation ahead of schedule. The site was left clean and ready for the next stage. I wouldn't hesitate to use them again or recommend them to others in the industry.</p>
  <div class="abs testi__name">Nora Pell</div>
  <div class="abs testi__role">CEO Pell Industries</div>
  <div class="abs dots" style="left:498px;top:3243px"><span></span><span></span><span></span></div>
</section>

<section>
  <div class="abs video" role="img" aria-label="Aerial view of a Sydney suburb beside the harbour"></div>
  <div class="abs video__play"><svg width="32" height="36" viewBox="0 0 32 36"><path d="M2 2l28 16L2 34z" fill="#86c440"/></svg></div>
</section>

<footer>
  <div class="abs footer-brand">
    <div class="footer-brand__logo">Harbourgate Earthmoving</div>
    <small>CALL US TODAY</small>
    <div class="footer-brand__phone">+61 400 555 124</div>
    <div class="footer-brand__social"><span></span><span></span><span></span><span></span></div>
    <p>Harbourgate Earthmoving is a trusted Sydney-based earthworks and excavation company.</p>
  </div>
  <div class="abs footer-main"></div>
  <div class="abs fcol" style="left:530px"><h4>Quick Links</h4><ul><li>About Company</li><li>Our Services</li><li>Our Projects</li><li>Plant Hire</li><li>Contacts</li></ul></div>
  <div class="abs fcol" style="left:669px"><h4>Clients Support</h4><ul><li>Careers</li><li>Our Process</li><li>FAQs</li><li>Clients Testimonials</li><li>Our Blog</li></ul></div>
  <div class="abs fcol news" style="left:819px;width:170px"><h4>Our News</h4>
    <h5>Agile Construction Management Building</h5><small>20 Nov 2025 &nbsp;&nbsp; by fieldnotes</small>
    <h5>Top Saas Construction Products Information</h5><small>20 Nov 2025 &nbsp;&nbsp; by fieldnotes</small>
    <div class="footer-dots"><span></span><span></span><span></span></div>
  </div>
  <div class="abs copyright">2025 © Harbourgate Earthmoving. All rights reserved</div>
</footer>

</body>
</html>
```